rk ironcraft business card metallic look

revamp the existing design but want card to have a metalic look to it

Target Market(s)

construction industry

Industry/Entity Type

constrction

Contact Information for Business Card

front of card RK Ironcraft, phone 4165550193, email rk.ironcraftt@veltrano.com and instagram account; rk_ironcraft_

Font styles to use
Other font styles liked:
• masculine

Colors

Designer to choose only greyscale colors for use in the design.

Requirements
Must have
• back side RK Ironcraft then a list of everything : Siding, ACM Panels, Standing Seam,Soffit, Fascia, Gutters,Metal,Alu,inum, Viynyl, Metal Roofs and roof repairs
Nice to have
• I would like to keep the look of the existing card with the metal grids on the front
Should not have
• Need a design in two days

```html
<!DOCTYPE html>
<html lang="en">
<head>
<meta charset="utf-8">
<title>RK Ironcraft – Business Card</title>
<link href="https://fonts.googleapis.com/css2?family=Oswald:wght@700&family=Signika:wght@700&display=swap" rel="stylesheet">
<style>
  :root {
    --page: #ffffff;
    --front-bg: #6d6e71;
    --back-bg: #d1d2d4;
    --steel-light: #f1f2f2;
    --steel-mid: #bcbec0;
    --steel-dark: #414042;
    --ink: #3a3a3c;
    --edge: #58595b;
  }
  * { margin: 0; padding: 0; box-sizing: border-box; }
  html, body { width: 1005px; height: 1200px; overflow: hidden; background: var(--page); }
  .sheet { position: relative; width: 1005px; height: 1200px; }
  .card {
    position: absolute; left: 1px; width: 1003px; height: 571px;
    border: 1px solid var(--edge); overflow: hidden;
  }
  .card--front { top: 1px; background: var(--front-bg); }
  .card--back { top: 628px; background: var(--back-bg); }
  .card__folds { position: absolute; inset: 0; width: 100%; height: 100%; }
  .brand {
    position: absolute; left: 0; right: 0; text-align: center;
    font-family: "Oswald", sans-serif; font-weight: 700; text-transform: uppercase;
    line-height: 1;
  }
  .card--front .brand { top: 96px; color: var(--steel-light); }
  .card--back .brand { top: 52px; color: var(--ink); }
  .brand__initials { display: block; font-size: 132px; letter-spacing: 6px; }
  .brand__word { display: block; font-size: 58px; letter-spacing: 15px; margin-top: 6px; padding-left: 15px; }
  .contact { position: absolute; left: 296px; top: 330px; }
  .contact__row { display: flex; align-items: center; height: 48px; margin-bottom: 2px; }
  .contact__icon { width: 44px; flex: none; display: flex; justify-content: center; margin-right: 20px; }
  .contact__text {
    font-family: "Signika", sans-serif; font-weight: 700; color: var(--steel-light);
    -webkit-text-stroke: 3px var(--steel-dark); paint-order: stroke fill;
  }
  .contact__text--phone { font-family: "Oswald", sans-serif; font-size: 34px; letter-spacing: 5px; }
  .contact__text--small { font-size: 22px; }
  .handle-mark { width: 34px; height: 34px; border: 3px solid var(--steel-dark); background: var(--steel-light); border-radius: 7px; }
  .services {
    position: absolute; left: 0; right: 0; top: 272px; text-align: center;
    font-family: "Signika", sans-serif; font-weight: 700; font-size: 38px; line-height: 54px;
    color: var(--steel-dark); -webkit-text-stroke: 6px var(--steel-light); paint-order: stroke fill;
  }
</style>
</head>
<body>
<main class="sheet">
  <section class="card card--front" aria-label="Card front">
    <svg class="card__folds" viewBox="0 0 1568 891" preserveAspectRatio="none" aria-hidden="true">
      <defs>
        <linearGradient id="foldDark" x1="0" y1="0" x2="1" y2="1">
          <stop offset="0" stop-color="#e6e7e8"/><stop offset="0.5" stop-color="#9d9fa2"/><stop offset="1" stop-color="#6d6e71"/>
        </linearGradient>
        <linearGradient id="foldDarkR" x1="1" y1="0" x2="0" y2="1">
          <stop offset="0" stop-color="#e6e7e8"/><stop offset="0.5" stop-color="#9d9fa2"/><stop offset="1" stop-color="#6d6e71"/>
        </linearGradient>
      </defs>
      <polygon points="0,0 275,0 0,230" fill="#77787b"/>
      <polygon points="0,220 265,0 275,0 0,232" fill="url(#foldDark)"/>
      <polygon points="1568,0 1295,0 1568,230" fill="#77787b"/>
      <polygon points="1568,220 1305,0 1295,0 1568,232" fill="url(#foldDarkR)"/>
      <polygon points="0,475 275,685 230,685 0,555" fill="url(#foldDark)"/>
      <polygon points="1568,475 1295,685 1340,685 1568,555" fill="url(#foldDarkR)"/>
      <polygon points="0,555 410,891 0,891" fill="url(#foldDark)" opacity="0.55"/>
      <polygon points="1568,555 1160,891 1568,891" fill="url(#foldDarkR)" opacity="0.55"/>
    </svg>
    <h1 class="brand"><span class="brand__initials">RK</span><span class="brand__word">Ironcraft</span></h1>
    <ul class="contact" style="list-style:none">
      <li class="contact__row">
        <span class="contact__icon">
          <svg width="40" height="40" viewBox="0 0 24 24" aria-hidden="true"><path d="M6.6 10.8c1.4 2.8 3.8 5.1 6.6 6.6l2.2-2.2c.3-.3.7-.4 1-.2 1.1.4 2.3.6 3.6.6.6 0 1 .4 1 1V20c0 .6-.4 1-1 1C10.6 21 3 13.4 3 4c0-.6.4-1 1-1h3.5c.6 0 1 .4 1 1 0 1.3.2 2.5.6 3.6.1.3 0 .7-.2 1z" fill="#f1f2f2" stroke="#414042" stroke-width="1.2"/></svg>
        </span>
        <span class="contact__text contact__text--phone">416-555-0193</span>
      </li>
      <li class="contact__row">
        <span class="contact__icon">
          <svg width="38" height="28" viewBox="0 0 38 28" aria-hidden="true"><rect x="1.5" y="1.5" width="35" height="25" fill="#f1f2f2" stroke="#414042" stroke-width="2"/><path d="M1.5 1.5 19 16 36.5 1.5M1.5 26.5 14 12M36.5 26.5 24 12" fill="none" stroke="#414042" stroke-width="1.5"/></svg>
        </span>
        <span class="contact__text contact__text--small">rk.ironcraftt@veltrano.com</span>
      </li>
      <li class="contact__row">
        <span class="contact__icon"><span class="handle-mark"></span></span>
        <span class="contact__text contact__text--small">rk_ironcraft_</span>
      </li>
    </ul>
  </section>

  <section class="card card--back" aria-label="Card back">
    <svg class="card__folds" viewBox="0 0 1568 891" preserveAspectRatio="none" aria-hidden="true">
      <defs>
        <linearGradient id="foldLight" x1="0" y1="0" x2="1" y2="1">
          <stop offset="0" stop-color="#f1f2f2"/><stop offset="0.5" stop-color="#a7a9ac"/><stop offset="1" stop-color="#d1d2d4"/>
        </linearGradient>
        <linearGradient id="foldLightR" x1="1" y1="0" x2="0" y2="1">
          <stop offset="0" stop-color="#f1f2f2"/><stop offset="0.5" stop-color="#a7a9ac"/><stop offset="1" stop-color="#d1d2d4"/>
        </linearGradient>
      </defs>
      <polygon points="0,460 410,795 360,795 0,540" fill="url(#foldLight)"/>
      <polygon points="1568,460 1160,795 1210,795 1568,540" fill="url(#foldLightR)"/>
      <polygon points="0,540 360,795 0,891" fill="#c7c8ca"/>
      <polygon points="1568,540 1210,795 1568,891" fill="#c7c8ca"/>
    </svg>
    <h2 class="brand"><span class="brand__initials">RK</span><span class="brand__word">Ironcraft</span></h2>
    <p class="services">Siding, ACM Panels, Standing Seam,<br>Soffit, Fascia, Gutters, Metal,<br>Aluminum, Vynyl, Metal Roof And<br>Roffing Repairs</p>
  </section>
</main>
</body>
</html>
```